Red Gum Wrecking P/L business card

I already have a EPS logo design that I wish to use however, the company is a demolition company based on the Central Coast of NSW Australia. The company is called "Red Gum Wrecking P/L".

We offer demolition services such as Residential, Commercial, Civil, Asbestos removal, Excavation and Tree removal that are required to be displayed on the rear of the business card.

We currently have 4 personnel that require business cards with their specific contact details.

The logo is mid blue on a white background and the remainder is black text on a whiter card.

The eps logo supplied should only be displayed as a logo without the text.

Target Market(s)

People, governments, companies requiring demolition services on the east coast of NSW, specifically Central Coast, Sydney and Newcastle locations.

Industry/Entity Type

Business

Contact Information for Business Card

There are four cards required
First card:
Martin Elsby
Operations Director
Mobile No. 0462 815094
E: info@redgumwreck.com.au
www.redgumwreck.com.au
Second card:
Peter Halloran
Project Director
Company Mobile: 0462 815094
Personal Mobile: 0428 160 384
www.redgumwreck.com.au
Third card:
Simon Preddy
Project Director
Company Mobile: 0462 815 094
Personal Mobile: 0433 958217
www.redgumwreck.com.au
Fourth card:
Neil Brathwaite
General Manager
Personal Mobile: 0437 281609
www.redgumwreck.com.au

Font styles to use
Other font styles liked:
• Helvetica

Colors
33a6d7

Requirements
Must have
• The RGW logo (without the text of Red Gum Wrecking)
Horizontal layout with logo on top left hand corner
Services provision on the rear of the card
Nice to have
• Logo on top left corner
Text should be something like Helvetica
Should not have
• Do not include the text that is incorporated in the EPS file I sent ….just the logo

```html
<!DOCTYPE html>
<html lang="en">
<head>
<meta charset="utf-8">
<title>Red Gum Wrecking P/L – Business Card</title>
<link rel="stylesheet" href="https://fonts.googleapis.com/css2?family=Comfortaa:wght@300;400&family=Arimo:wght@400;700&display=swap">
<style>
  :root {
    --brand-blue: #58b3d6;
    --ink: #111111;
    --muted: #9a9a9a;
    --crop: #555555;
    --sheet: #ffffff;
    --card-edge: #ececec;
    --on-blue: #ffffff;
  }
  * { margin: 0; padding: 0; box-sizing: border-box; }
  html, body { width: 1200px; height: 411px; overflow: hidden; background: var(--sheet); }
  .sheet { position: relative; width: 1200px; height: 411px; font-family: "Arimo", Helvetica, Arial, sans-serif; }
  .crop-marks { position: absolute; inset: 0; }
  .side-label { position: absolute; top: 52px; font-size: 17px; color: var(--ink); transform: translateX(-50%); }
  .card { position: absolute; }
  .card--front { left: 59px; top: 101px; width: 416px; height: 251px; background: #fff; border: 1px solid var(--card-edge); }
  .card--back { left: 722px; top: 109px; width: 416px; height: 254px; background: var(--brand-blue); }
  .brand-lockup { position: absolute; display: flex; align-items: center; }
  .brand-mark { font-family: "Comfortaa", sans-serif; font-weight: 400; font-size: 30px; letter-spacing: 1px; width: 76px; }
  .brand-divider { width: 1px; height: 58px; margin: 0 10px 0 8px; }
  .brand-title { font-family: "Comfortaa", sans-serif; font-weight: 300; line-height: 1.45; font-size: 15px; }
  .card--front .brand-lockup { left: 20px; top: 15px; }
  .card--front .brand-mark { color: var(--brand-blue); }
  .card--front .brand-divider { background: var(--muted); }
  .card--front .brand-title { color: var(--muted); }
  .card--front .brand-title .person { color: var(--brand-blue); }
  .card--back .brand-lockup { left: 110px; top: 95px; }
  .card--back .brand-mark, .card--back .brand-title { color: var(--on-blue); }
  .card--back .brand-mark { font-size: 24px; width: 56px; }
  .card--back .brand-divider { background: var(--on-blue); height: 50px; margin: 0 8px 0 6px; }
  .card--back .brand-title { font-size: 13px; }
  .services { position: absolute; left: 0; right: 0; bottom: 22px; text-align: center; color: var(--on-blue); font-size: 10px; letter-spacing: 0.3px; }
  .services li { display: inline; list-style: none; }
  .services li + li::before { content: "·"; margin: 0 6px; }
  .contact { position: absolute; left: 20px; top: 137px; font-size: 10px; line-height: 1.2; }
  .contact .name { color: var(--brand-blue); font-weight: 700; font-size: 11px; }
  .contact .title { color: var(--muted); margin-bottom: 13px; }
  .contact .line { color: var(--ink); }
  .contact .label { color: var(--brand-blue); font-weight: 700; }
  .contact .web { color: var(--brand-blue); font-weight: 700; }
  .corner-tile { position: absolute; left: 450px; top: 324px; width: 39px; height: 39px; background: var(--brand-blue); }
</style>
</head>
<body>
<div class="sheet">
  <svg class="crop-marks" width="1200" height="411" viewBox="0 0 1200 411" aria-hidden="true">
    <g stroke="var(--crop)" stroke-width="1" fill="none">
      <line x1="0" y1="101" x2="59" y2="101"/>
      <line x1="475" y1="101" x2="536" y2="101"/>
      <line x1="0" y1="352" x2="59" y2="352"/>
      <line x1="475" y1="352" x2="536" y2="352"/>
      <line x1="59" y1="39" x2="59" y2="101"/>
      <line x1="59" y1="352" x2="59" y2="411"/>
      <line x1="475" y1="39" x2="475" y2="101"/>
      <line x1="475" y1="352" x2="475" y2="411"/>
      <line x1="667" y1="109" x2="722" y2="109"/>
      <line x1="1138" y1="109" x2="1200" y2="109"/>
      <line x1="667" y1="363" x2="722" y2="363"/>
      <line x1="1138" y1="363" x2="1200" y2="363"/>
      <line x1="722" y1="47" x2="722" y2="109"/>
      <line x1="722" y1="363" x2="722" y2="411"/>
      <line x1="1138" y1="47" x2="1138" y2="109"/>
      <line x1="1138" y1="363" x2="1138" y2="411"/>
    </g>
  </svg>

  <div class="side-label" style="left:222px">Front</div>
  <div class="side-label" style="left:945px">Back</div>

  <section class="card card--front">
    <div class="brand-lockup">
      <div class="brand-mark">RGW</div>
      <div class="brand-divider"></div>
      <div class="brand-title">
        <div class="person">martinElsby</div>
        <div class="role">operations director</div>
      </div>
    </div>
    <div class="contact">
      <div class="name">Martin Elsby</div>
      <div class="title">Operations Director</div>
      <div class="line"><span class="label">t:</span> 0462 815094</div>
      <div class="line"><span class="label">e:</span> info@redgumwreck.com.au</div>
      <div class="web">www.redgumwreck.com.au</div>
    </div>
  </section>
  <div class="corner-tile"></div>

  <section class="card card--back">
    <div class="brand-lockup">
      <div class="brand-mark">RGW</div>
      <div class="brand-divider"></div>
      <div class="brand-title">
        <div class="person">martinElsby</div>
        <div class="role">operations director</div>
      </div>
    </div>
    <ul class="services">
      <li>Residential</li><li>Commercial</li><li>Civil</li><li>Asbestos Removal</li><li>Excavation</li><li>Tree Removal</li>
    </ul>
  </section>
</div>
</body>
</html>
```